Web Design for Harbor Ledger Allies

Harbor Ledger Allies needs the photoshop files for a simple, clean and professional website design. The company is building a network of bookkeepers/accountants to handle outsourced bookkeeping services for start ups and small businesses. It needs to both attract bookkeepers to become partners and give clients confidence in the professional network. The partners will use products like Tallymint Web, Brightfolio.example and PennyTrim.example for start ups, as well as help with tasks using the clients existing accounting software.

A home and subpage design is needed. I'll award the work based on the home design. The minor subpage changes can be worked out in the workroom stage.

The pages for the navigation will be: Home, Services, Locations, Partners, FAQ, Contact

```html
<!DOCTYPE html>
<html lang="en">
<head>
<meta charset="utf-8">
<title>Harbor Ledger Allies — Home</title>
<link rel="stylesheet" href="https://fonts.googleapis.com/css2?family=Quicksand:wght@400;500;600&display=swap">
<style>
  :root {
    --white: #ffffff;
    --ink: #4a4a4a;
    --nav-grey: #8a8a8a;
    --brand-blue: #3aa3dc;
    --tab-deep: #1e9ad6;
    --tab-mid: #6cbfe9;
    --tab-pale: #a9d9f2;
    --hero-light: #f4f6f7;
    --hero-mid: #e3e7ea;
    --shirt-blue: #b9d3ea;
  }
  * { margin: 0; padding: 0; box-sizing: border-box; }
  html, body {
    width: 1200px; height: 800px; overflow: hidden;
    background: var(--white);
    font-family: "Quicksand", sans-serif;
  }
  .page { position: relative; width: 1200px; height: 800px; overflow: hidden; }

  .site-header {
    position: absolute; top: 0; left: 0; width: 1200px; height: 88px;
    background: var(--white);
    display: flex; align-items: center; justify-content: space-between;
    padding: 0 190px 0 176px; z-index: 3;
  }
  .brand { display: flex; align-items: center; gap: 12px; }
  .brand-mark { width: 30px; height: 30px; border-radius: 50%; background: var(--brand-blue); }
  .brand-name {
    width: 120px; font-size: 13px; line-height: 14px; font-weight: 600;
    letter-spacing: 0.5px; text-transform: uppercase; color: var(--brand-blue);
  }
  .main-nav { display: flex; gap: 24px; list-style: none; }
  .main-nav a {
    font-size: 11px; font-weight: 500; letter-spacing: 1px;
    text-transform: uppercase; color: var(--nav-grey); text-decoration: none;
  }

  .hero {
    position: absolute; top: 88px; left: 0; width: 1200px; height: 652px;
    background: linear-gradient(90deg, var(--hero-mid) 0%, var(--hero-light) 45%, var(--white) 75%, var(--hero-light) 100%);
  }
  .hero-portrait {
    position: absolute; left: 660px; top: 60px; width: 360px; height: 592px;
    background: linear-gradient(180deg, #dfe4e8 0%, var(--shirt-blue) 45%, #a8c6e2 100%);
    border-radius: 180px 180px 0 0;
  }
  .hero-copy { position: absolute; left: 203px; top: 160px; width: 420px; }
  .hero-title {
    font-size: 40px; line-height: 48px; font-weight: 400; color: var(--brand-blue);
  }
  .hero-text {
    margin-top: 28px; font-size: 15px; line-height: 22px; color: var(--ink);
  }
  .hero-button {
    display: inline-block; margin-top: 40px; padding: 10px 26px;
    border: 2px solid var(--brand-blue); border-radius: 12px;
    font-size: 20px; font-weight: 500; letter-spacing: 1px;
    color: var(--brand-blue); text-decoration: none;
  }

  .section-tabs { position: absolute; left: 215px; top: 676px; width: 900px; height: 124px; z-index: 2; }
  .section-tab {
    position: absolute; bottom: 0; color: var(--white);
    font-size: 15px; font-weight: 500; text-align: center; padding-top: 24px;
  }
  .tab-what { left: 0; width: 330px; height: 110px; background: var(--tab-deep); }
  .tab-where { left: 330px; width: 330px; height: 118px; background: var(--tab-mid); }
  .tab-work { left: 660px; width: 240px; height: 124px; background: var(--tab-pale); }
</style>
</head>
<body>
<div class="page">
  <header class="site-header">
    <div class="brand">
      <span class="brand-mark"></span>
      <span class="brand-name">Harbor Ledger Allies</span>
    </div>
    <nav>
      <ul class="main-nav">
        <li><a href="#">Services</a></li>
        <li><a href="#">Locations</a></li>
        <li><a href="#">Partners</a></li>
        <li><a href="#">FAQ</a></li>
        <li><a href="#">Contact</a></li>
      </ul>
    </nav>
  </header>

  <section class="hero">
    <div class="hero-portrait" role="img" aria-label="Photo of a smiling bookkeeper in a light blue shirt holding a laptop, in a bright blurred office"></div>
    <div class="hero-copy">
      <h1 class="hero-title">We Handle<br>Your Bookeeping</h1>
      <p class="hero-text">Lorem Ipsum is simply dummy text of the printing and typesetting industry. Lorem Ipsum has been the industry's standard dummy text ever since the 1500s, when an unknown.</p>
      <a class="hero-button" href="#">START NOW</a>
    </div>
  </section>

  <nav class="section-tabs">
    <div class="section-tab tab-what">What we do</div>
    <div class="section-tab tab-where">Where to find us</div>
    <div class="section-tab tab-work">Work with us</div>
  </nav>
</div>
</body>
</html>
```